Walking in Grace book cover

Needing a book cover design and I have attached 3 sample covers for a starting point. I would like the design to use similar font as the sample cover along with a red and white theme. I would like a background image of broken shackles. On the back cover leave room for the author's bio and picture. The front cover and book details are below:
Book size: 6x9 or. 4.5x7
Title: Walking in Grace
Subtitle: Standing Firm Against Every Snare Through Scripture
Author: Marlon Petway
No spine is needed for the book due to it is a smaller book and the text will not fit. Yes, we are looking at every design and will choose winner on or before 4/20/2022

```html
<!DOCTYPE html>
<html lang="en">
<head>
<meta charset="utf-8">
<title>Walking in Grace — Book Cover</title>
<link rel="stylesheet" href="https://fonts.googleapis.com/css2?family=Cinzel:wght@400;500;600&display=swap">
<style>
  :root {
    --paper: #f7f4ee;
    --paper-shade: #e9e3d8;
    --title-red: #b3191b;
    --author-white: #fdfbf7;
    --warm-orange: #c8632a;
    --warm-brown: #7a3a1e;
    --warm-gold: #d9a24a;
  }
  html, body {
    margin: 0;
    padding: 0;
    width: 750px;
    height: 1200px;
    overflow: hidden;
    background: var(--paper);
  }
  .cover {
    position: relative;
    width: 750px;
    height: 1200px;
    overflow: hidden;
    background:
      radial-gradient(ellipse at 50% 45%, #ffffff 0%, var(--paper) 55%, var(--paper-shade) 100%);
    font-family: "Cinzel", serif;
  }
  .cover-art {
    position: absolute;
    left: 0;
    top: 470px;
    width: 750px;
    height: 730px;
    background:
      radial-gradient(ellipse 32% 55% at 50% 38%, rgba(255,255,255,1) 0%, rgba(255,255,255,0.85) 45%, rgba(255,255,255,0) 100%),
      linear-gradient(90deg, var(--warm-brown) 0%, var(--warm-orange) 18%, var(--warm-gold) 32%, rgba(255,255,255,0.6) 50%, var(--warm-gold) 68%, var(--warm-orange) 82%, var(--warm-brown) 100%);
    -webkit-mask-image: linear-gradient(180deg, transparent 0%, #000 22%, #000 100%);
    mask-image: linear-gradient(180deg, transparent 0%, #000 22%, #000 100%);
  }
  .title-block {
    position: absolute;
    top: 96px;
    left: 0;
    width: 100%;
    text-align: center;
    color: var(--title-red);
  }
  .title-lead {
    margin: 0;
    font-size: 74px;
    font-weight: 500;
    letter-spacing: 4px;
    line-height: 1;
  }
  .title-main {
    margin: 18px 0 0;
    font-size: 186px;
    font-weight: 500;
    letter-spacing: 6px;
    line-height: 1;
  }
  .subtitle {
    margin: 44px 0 0;
    font-size: 20px;
    font-weight: 400;
    letter-spacing: 1.5px;
    line-height: 1.85;
  }
  .author {
    position: absolute;
    left: 0;
    bottom: 56px;
    width: 100%;
    margin: 0;
    text-align: center;
    color: var(--author-white);
    font-size: 66px;
    font-weight: 500;
    letter-spacing: 3px;
    line-height: 1;
    text-shadow: 0 2px 6px rgba(60, 25, 10, 0.75), 0 0 18px rgba(60, 25, 10, 0.45);
  }
</style>
</head>
<body>
  <main class="cover">
    <div class="cover-art" role="img" aria-label="Painted illustration of two raised hands breaking free from iron shackles, with a burst of white light between them"></div>

    <header class="title-block">
      <h1 class="title-lead">WALKING IN</h1>
      <p class="title-main">GRACE</p>
      <p class="subtitle">STANDING FIRM AGAINST EVERY SNARE<br>THROUGH SCRIPTURE</p>
    </header>

    <p class="author">MARLON PETWAY</p>
  </main>
</body>
</html>
```